KestrelNet Business Cards

Create business cards for our exciting new software company. We provide cloud billing systems and provisioning software for campany that need monthly SaaS and Cloud Billing

Target Market(s)

Enterprise businesses, b2b, telecom carriers, software manufactures

Industry/Entity Type

Software

```html
<!DOCTYPE html>
<html lang="en">
<head>
<meta charset="utf-8">
<title>KestrelNet Business Cards</title>
<link rel="stylesheet" href="https://fonts.googleapis.com/css2?family=Arimo:wght@400;700&display=swap">
<style>
  :root {
    --page: #ffffff;
    --ink: #000000;
    --brand: #1d4f9c;
    --brand-light: #2a8fd8;
    --sky: #8fd0ff;
    --deep: #0d3a8c;
    --cream: #f4f1e6;
    --beige: #dcd6bd;
    --grey: #9a9a9a;
    --faint: #c9dcef;
    --frame: #6ec6f2;
    --white: #ffffff;
  }
  * { margin: 0; padding: 0; box-sizing: border-box; }
  html, body { width: 1200px; height: 936px; overflow: hidden; background: var(--page); }
  body { position: relative; font-family: "Arimo", Arial, sans-serif; }

  .label { position: absolute; font-size: 50px; color: var(--ink); line-height: 1; }

  .card { position: absolute; overflow: hidden; }
  .card svg.bg { position: absolute; inset: 0; width: 100%; height: 100%; }
  .card .layer { position: absolute; }

  .brand { position: absolute; display: flex; align-items: center; gap: 5px; }
  .brand .dot { width: 12px; height: 12px; border-radius: 50%; background: var(--brand-light); }
  .brand .name { font-weight: 700; font-size: 15px; color: var(--brand); }
  .brand-tag { position: absolute; font-size: 5px; color: var(--brand); letter-spacing: .2px; }

  .txt { position: absolute; font-size: 10.5px; line-height: 1.3; }
  .tiny { position: absolute; font-size: 6.5px; line-height: 1.35; color: var(--brand-light); text-align: center; }

  /* card 1 */
  .c1-front { left: 160px; top: 0; width: 361px; height: 208px; background: var(--cream); }
  .c1-front .headline { left: 211px; top: 82px; font-weight: 700; font-size: 16px; color: var(--white); }
  .c1-front .site { left: 211px; top: 102px; color: var(--white); }
  .c1-front .contact { left: 205px; top: 124px; color: var(--white); }
  .c1-back { left: 160px; top: 222px; width: 361px; height: 208px;
             background: linear-gradient(90deg, var(--cream), var(--beige)); }

  /* card 2 */
  .c2-front { left: 727px; top: 14px; width: 354px; height: 202px; background: var(--white); border: 1px solid var(--ink); }
  .c2-front .person { right: 14px; top: 92px; color: var(--white); text-align: right; }
  .c2-front .contact { left: 210px; top: 130px; color: var(--white); }
  .c2-back { left: 727px; top: 250px; width: 354px; height: 202px; background: var(--white); border: 1px solid var(--ink); }
  .c2-back .mark { left: 110px; top: 55px; font-size: 56px; font-weight: 700; color: var(--faint); white-space: nowrap; }

  /* vertical pair */
  .v-back { left: 364px; top: 598px; width: 208px; height: 336px;
            background: radial-gradient(circle at 52% 29%, #ffffff 0%, #bfe6ff 14%, #3d8fe0 42%, var(--deep) 80%); }
  .v-back .small { left: 0; width: 100%; top: 278px; color: var(--white); font-size: 6px; text-align: center; line-height: 1.4; }
  .v-back .site { left: 0; width: 100%; top: 312px; color: var(--white); font-size: 8px; text-align: center; }
  .v-front { left: 621px; top: 598px; width: 208px; height: 336px; background: var(--white); border: 1.5px solid var(--frame); }
  .v-front .person { right: 38px; top: 196px; color: var(--brand-light); text-align: right; }
  .v-front .contact { left: 40px; top: 238px; color: var(--brand-light); }
</style>
</head>
<body>
  <div class="label" style="left:0;top:74px">Front</div>
  <div class="label" style="left:0;top:312px">Back</div>
  <div class="label" style="left:584px;top:74px">Front</div>
  <div class="label" style="left:584px;top:326px">Back</div>
  <div class="label" style="left:413px;top:526px">Back</div>
  <div class="label" style="left:667px;top:526px">Front</div>

  <!-- Card one, front -->
  <section class="card c1-front">
    <svg class="bg" viewBox="0 0 361 208" preserveAspectRatio="none">
      <defs>
        <linearGradient id="c1-sweep" x1="0" y1="0" x2="1" y2="1">
          <stop offset="0" stop-color="#5fb2f2"/>
          <stop offset="1" stop-color="#0e3d9c"/>
        </linearGradient>
      </defs>
      <path d="M0,208 Q150,30 361,0 L361,208 Z" fill="#7dc3f5"/>
      <path d="M20,208 Q170,50 361,14 L361,208 Z" fill="url(#c1-sweep)"/>
      <path d="M140,208 Q260,150 361,130 L361,208 Z" fill="#0b2f86" opacity=".6"/>
    </svg>
    <div class="brand" style="left:14px;top:54px"><span class="dot"></span><span class="name">KestrelNet</span></div>
    <div class="brand-tag" style="left:31px;top:74px">cloud billing software</div>
    <div class="layer headline">Sample Text</div>
    <div class="txt site">www.yourwebsite.com</div>
    <div class="txt contact">Address: Text text text text<br>text text text text text<br>Tel.: +00 000 000 00 00<br>Fax.: +00 000 000 00 00<br>office@yourwebsite.com</div>
  </section>

  <!-- Card one, back -->
  <section class="card c1-back">
    <div class="tiny" style="left:0;width:100%;top:82px">your text here your text here<br>your text here your text here your text here<br>your text here your text</div>
    <div class="brand" style="left:112px;top:126px"><span class="dot"></span><span class="name">KestrelNet</span></div>
    <div class="brand-tag" style="left:129px;top:146px">cloud billing software</div>
    <div class="txt" style="left:0;width:100%;text-align:center;top:168px;color:var(--brand-light);font-size:9px;font-weight:700">www.yourwebsite.com</div>
  </section>

  <!-- Card two, front -->
  <section class="card c2-front">
    <svg class="bg" viewBox="0 0 354 202" preserveAspectRatio="none">
      <defs>
        <radialGradient id="c2-glow" cx=".55" cy=".25" r=".7">
          <stop offset="0" stop-color="#d9f0ff"/>
          <stop offset=".5" stop-color="#4f9fe8"/>
          <stop offset="1" stop-color="#1f5fc4"/>
        </radialGradient>
        <linearGradient id="c2-grey" x1="0" y1="0" x2="1" y2="0">
          <stop offset="0" stop-color="#e4e4e4"/>
          <stop offset="1" stop-color="#8a8a8a"/>
        </linearGradient>
      </defs>
      <path d="M0,202 Q80,110 354,100 L354,202 Z" fill="url(#c2-grey)"/>
      <path d="M110,0 Q170,120 354,125 L354,0 Z" fill="url(#c2-glow)"/>
    </svg>
    <div class="brand" style="left:31px;top:60px"><span class="dot"></span><span class="name">KestrelNet</span></div>
    <div class="brand-tag" style="left:48px;top:80px">cloud billing software</div>
    <div class="txt person">First and Last Name<br>Post</div>
    <div class="txt contact">Address: Text text text text<br>text text text text text<br>Tel.: +00 000 000 00 00<br>Fax.: +00 000 000 00 00<br>office@yourwebsite.com</div>
  </section>

  <!-- Card two, back -->
  <section class="card c2-back">
    <div class="layer mark" aria-hidden="true">KestrelNet</div>
    <div class="tiny" style="left:96px;top:78px;text-align:left">your text here your text here<br>your text here your text here your text here<br>your text here your text</div>
    <div class="brand" style="left:92px;top:122px"><span class="dot"></span><span class="name">KestrelNet</span></div>
    <div class="brand-tag" style="left:109px;top:142px">cloud billing software</div>
    <div class="txt" style="left:92px;top:162px;color:var(--brand-light);font-size:9px;font-weight:700">www.yourwebsite.com</div>
  </section>

  <!-- Vertical card, back -->
  <section class="card v-back">
    <div class="brand" style="left:52px;top:100px"><span class="dot"></span><span class="name">KestrelNet</span></div>
    <div class="brand-tag" style="left:69px;top:120px">cloud billing software</div>
    <div class="layer small">SAMPLE YOUR TEXT HERE<br>YOUR TEXT SAMPLE HERE<br>PLACE TEXT HERE</div>
    <div class="layer site">www.yourwebsite.com</div>
  </section>

  <!-- Vertical card, front -->
  <section class="card v-front">
    <div class="brand" style="left:52px;top:94px"><span class="dot"></span><span class="name">KestrelNet</span></div>
    <div class="brand-tag" style="left:69px;top:114px">cloud billing software</div>
    <div class="txt person">First and Last Name<br>Post</div>
    <div class="txt contact">Address: Text text text<br>text text text text text<br>Tel.: +00 000 000 00 00<br>Fax.: +00 000 000 00 00<br>office@yourwebsite.com</div>
  </section>
</body>
</html>
```